Organic, Vegan friendly and luxurious face moisturiser branding needed

Hi team

We are in the process of launching an all organic, no nasties facial moisturiser that will suite both men and woman.
We have narrowed down the bottle packaging and box packaging but need to clarify the dimensions, however we are happy to start with a few concepts. We need artwork for both the bottle and box to be designed.

The bottle will be a gloss white finish with a white dispensing pump on top. We would like to keep the colour scheme as clean as possible as the final design will be printed directly onto the bottle.
We would like to keep all text and artwork black however we are happy to explore a few shades of darker grey in the design as well.

Overall the message we want to convey through the art is one of Luxury, Pinnacle brand, eco friendliness and Organic.

Attached is a few images of artwork we like, the bottle shape will be near identical.

The brand name will be : Vendra, which means Honest in Norwegian.
We would like the tagline "Uncomplicated Skincare" to be shown somewhere on the bottle.

Ideally the front design will show the name : Vendra - Organics
Tagline "uncomplicated skincare"
Facial Moisturiser
Some sort of picture depicting the ingredients, we like floral/botanical inspiration such as some of the images attached - Ideally we want some of our ingredients to shine one the front - Some of them include:

1. Organic Aloe
2. Organic Shea
3. Green tea
4. Organic Jojoba

At the bottom front of the bottle we you will also need to display the content size, which will be 100ml/ 3.3 FL OZ

At the back the list of ingredients needs to be shown.

Aloe Barbadensis Leaf Juice (Organic Aloe), Aqua (Water), Helianthus Annuus Seed Oil (Organic Sunflower), Isopropyl Palmitate, Glyceryl Stearate SE, Cetyl Alcohol, Stearic Acid, Glycerin ( Kosher Vegetable), Butyrospermum Parkii Butter (Organic Shea), Simmondsia Chinesis Seed Oil (Organic Jojoba), Panthenol (Vitamin B5), Tocopherol Acetate (Vitamin E), Camelia Sinensis Leaf Extract (Green Tea), Xanthane Gum, Phenoxyethanol, Ethylhexylglycerin..

Alongside this we want to list the following:

1. The product is Vegan friendly
2. No Animal Testing
3 .Kosher Certified
4. Sustainable Raw Materials
5. Powered with 100% Renewable Wind Energy
6. Certified organic

You can design little logos instead of writing it out.

Hi Everyone. Please use the following template for the information on the back of the bottle. Vendra How to use: Apply twice a day to face and throat all over, or where needed. For best results, thoroughly wash face prior to use. Ingredients: Aloe Barbadensis Leaf Juice (Organic Aloe), Aqua (Water), Helianthus Annuus Seed Oil (Organic Sunflower), Isopropyl Palmitate (Plant based), Glyceryl Stearate SE (Plant based), Cetyl Alcohol (Plant based), Stearic Acid (Plant based), Glycerin ( Kosher Vegetable), Butyrospermum Parkii Butter (Organic Shea), Simmondsia Chinesis Seed Oil (Organic Jojoba), Panthenol (Vitamin B5), Tocopherol Acetate (Vitamin E), Camelia Sinensis Leaf Extract (Green Tea),  Xanthan Gum (Plant based), Phenoxyethanol (Natural preservative), Ethylhexylglycerin (Plant based) Caution: For External use only. Avoid contact with eyes. If contact occurs, rinse thoroughly with water. Keep out of reach of children. This delightful lotion absorbs right into the skin without leaving a greasy feeling yet provides the glide of a deep penetrating moisturizer. It conditions your skin while it moisturizes and softens and will leave your skin glowing. Vendra Organics info@vendracosmetics.example Made in the USA

Industry/Entity Type

Cosmetics

Font styles to use
Serif
Sans Serif

Colors
5c5c5c
333333
000000
ffffff

Requirements
Must have
• Attached is the example of the clean bottle.
• Here are the dimensions of the bottle :
• Single Specs:
• White/White/White
• Weight: 39.67g
• Width: 47.48mm
• Height: 124.90mm
• Airless Bottle, White Cap, White Pump and Collar, White Body, 100mL

```html
<!DOCTYPE html>
<html lang="en">
<head>
<meta charset="utf-8">
<title>Vendra Facial Moisturiser – Front Label</title>
<link href="https://fonts.googleapis.com/css2?family=Montserrat:wght@400&display=swap" rel="stylesheet">
<style>
  :root {
    --label-white: #ffffff;
    --ink-mid: #5c5c5c;
    --ink-dark: #333333;
    --art-light: #eeeeee;
    --art-dark: #9a9a9a;
  }
  html, body {
    margin: 0;
    padding: 0;
    width: 964px;
    height: 1200px;
    overflow: hidden;
    background: var(--label-white);
  }
  .label {
    position: relative;
    width: 964px;
    height: 1200px;
    font-family: "Montserrat", sans-serif;
    font-weight: 400;
    color: var(--ink-mid);
  }
  .label > * {
    position: absolute;
    left: 0;
    right: 0;
    margin: 0;
    text-align: center;
  }
  .brand-name {
    top: 92px;
    font-weight: 400;
    font-size: 88px;
    line-height: 1;
    color: var(--ink-mid);
  }
  .tagline {
    top: 236px;
    font-size: 28px;
    line-height: 1.2;
    letter-spacing: 1px;
    color: var(--ink-dark);
  }
  .product-name {
    top: 323px;
    font-size: 38px;
    line-height: 1.2;
    color: var(--ink-mid);
  }
  .botanical-art {
    top: 402px;
    left: 226px;
    width: 512px;
    height: 512px;
  }
  .ingredient {
    top: 968px;
    font-size: 38px;
    line-height: 1.2;
    color: var(--ink-mid);
  }
  .volume {
    top: 1072px;
    font-size: 27px;
    line-height: 1.2;
    color: var(--ink-mid);
  }
</style>
</head>
<body>
  <main class="label">
    <h1 class="brand-name">Vendra</h1>
    <p class="tagline">Uncomplicated Skincare</p>
    <p class="product-name">Facial Moisturiser</p>
    <svg class="botanical-art" viewBox="0 0 512 512" role="img" aria-label="Grey botanical sketch of a jojoba branch with a leaf and two seed pods">
      <defs>
        <radialGradient id="artTone" cx="50%" cy="50%" r="55%">
          <stop offset="0%" stop-color="#9a9a9a" stop-opacity="0.5"/>
          <stop offset="100%" stop-color="#eeeeee" stop-opacity="0.4"/>
        </radialGradient>
      </defs>
      <rect x="0" y="0" width="512" height="512" fill="url(#artTone)"/>
    </svg>
    <p class="ingredient">Organic Jojoba</p>
    <p class="volume">100ml (3.3 fl oz)</p>
  </main>
</body>
</html>
```